Business card design needed

A laid back coffee shop that has a great feel, that becomes a bar and grill at night. We are also wanting to cater for functions etc.
The business itself is painted dark blue/charcoal and has red doors.
Would like a logo that will be recognised when seen.

Industry/Entity Type

Coffee Shop

Contact Information for Business Card

The Lantern Coffee Bar & Grill
14b Wattlebrook St
Kelmarra NSW 2318
Ph. 02 4817 6293

Logo Text

Logo styles of interest
Emblem Logo
Abstract Logo
Wordmark Logo
Requirements
Must have
• A loyalty card on the back with 2 rows of 7 stamp spaces and a place to write a name and phone number (for a draw)

```html
<!DOCTYPE html>
<html lang="en">
<head>
<meta charset="utf-8">
<title>The Lantern Coffee Bar &amp; Grill – Business &amp; Loyalty Card</title>
<link rel="stylesheet" href="https://fonts.googleapis.com/css2?family=Josefin+Sans:wght@300;400&family=Nunito+Sans:wght@400;700&display=swap">
<style>
  :root {
    --backdrop: #4a555b;
    --brand-blue: #0000cc;
    --emblem-tint: #5a6aae;
    --accent-red: #ee1111;
    --tagline-grey: #b3b6c6;
    --footer-grey: #a6a6a6;
    --ink: #111111;
    --paper: #ffffff;
    --stamp-line: #555555;
  }
  * { margin: 0; padding: 0; box-sizing: border-box; }
  html, body { width: 1200px; height: 1000px; overflow: hidden; }
  body {
    background: var(--backdrop);
    position: relative;
    font-family: "Nunito Sans", Arial, sans-serif;
  }
  .card {
    position: absolute;
    left: 204px;
    width: 780px;
    box-shadow: 2px 3px 4px rgba(0,0,0,0.55);
    overflow: hidden;
  }
  /* Front */
  .card-front {
    top: 47px;
    height: 421px;
    background: var(--brand-blue);
  }
  .emblem-area {
    position: absolute;
    left: 0; top: 0;
    width: 340px; height: 421px;
  }
  .wordmark {
    position: absolute;
    right: 38px;
    top: 168px;
    color: var(--paper);
    font-weight: 400;
    font-size: 80px;
    line-height: 1;
    letter-spacing: -1px;
    white-space: nowrap;
  }
  .wordmark-rule {
    position: absolute;
    left: 337px;
    top: 250px;
    width: 390px;
    height: 6px;
  }
  .tagline {
    position: absolute;
    left: 354px;
    top: 272px;
    width: 356px;
    text-align: center;
    font-family: "Josefin Sans", Arial, sans-serif;
    font-weight: 300;
    font-size: 25px;
    letter-spacing: 4px;
    color: var(--tagline-grey);
    white-space: nowrap;
  }
  /* Back */
  .card-back {
    top: 519px;
    left: 203px;
    width: 781px;
    height: 433px;
    background: var(--paper);
  }
  .draw-entry {
    position: absolute;
    left: 66px;
    top: 48px;
    width: 660px;
    height: 24px;
    display: flex;
    align-items: flex-end;
    color: var(--brand-blue);
    font-size: 17px;
  }
  .draw-entry .label { margin-right: 5px; line-height: 1; }
  .draw-entry .write-line {
    border-bottom: 1px solid var(--ink);
    height: 1px;
    margin-bottom: 3px;
  }
  .write-line.name { width: 245px; }
  .write-line.phone { width: 312px; }
  .phone-icon { width: 20px; height: 14px; margin: 0 9px 4px 9px; }
  .stamp-grid {
    position: absolute;
    left: 145px;
    top: 116px;
    display: grid;
    grid-template-columns: repeat(7, 72px);
    column-gap: 13px;
    row-gap: 14px;
  }
  .stamp {
    width: 72px;
    height: 72px;
    border-radius: 50%;
    border: 1px solid var(--stamp-line);
    background: var(--paper);
    position: relative;
  }
  .stamp::after {
    content: "";
    position: absolute;
    left: 14px;
    bottom: -9px;
    width: 44px;
    height: 7px;
    border-radius: 50%;
    background: radial-gradient(ellipse at center, rgba(0,0,0,0.28), rgba(0,0,0,0) 70%);
    z-index: -1;
  }
  .stamp-grid .stamp { z-index: 1; }
  .business-name {
    position: absolute;
    right: 57px;
    top: 324px;
    white-space: nowrap;
    line-height: 1;
  }
  .business-name .name {
    color: var(--brand-blue);
    font-weight: 700;
    font-size: 33px;
  }
  .business-name .descriptor {
    color: var(--footer-grey);
    font-size: 25px;
    margin-left: 6px;
  }
  .address {
    position: absolute;
    right: 59px;
    top: 366px;
    font-size: 23px;
    color: var(--ink);
    white-space: nowrap;
  }
</style>
</head>
<body>

<section class="card card-front">
  <svg class="emblem-area" role="img" aria-label="Large faint brand emblem area" viewBox="0 0 340 421">
    <defs>
      <radialGradient id="groundShadow" cx="50%" cy="50%" r="50%">
        <stop offset="0%" stop-color="#000033" stop-opacity="0.85"/>
        <stop offset="100%" stop-color="#000033" stop-opacity="0"/>
      </radialGradient>
    </defs>
    <ellipse cx="150" cy="360" rx="175" ry="32" fill="url(#groundShadow)"/>
    <circle cx="150" cy="215" r="140" fill="var(--emblem-tint)"/>
  </svg>
  <div class="wordmark">The Lantern</div>
  <svg class="wordmark-rule" viewBox="0 0 390 6" preserveAspectRatio="none">
    <path d="M0 3 Q195 -1 390 3 Q195 7 0 3 Z" fill="var(--accent-red)"/>
  </svg>
  <div class="tagline">COFFEE BAR &amp; GRILL</div>
</section>

<section class="card card-back">
  <div class="draw-entry">
    <span class="label">Name:</span>
    <span class="write-line name"></span>
    <svg class="phone-icon" viewBox="0 0 20 14" aria-label="Phone">
      <path d="M1 5 Q10 -1 19 5 L17 7 L14 5 L14 3 Q10 2 6 3 L6 5 L3 7 Z" fill="var(--brand-blue)"/>
      <path d="M5 7 L7 5 L13 5 L15 7 L16 13 L4 13 Z" fill="var(--brand-blue)"/>
      <circle cx="10" cy="9.5" r="2" fill="var(--paper)"/>
    </svg>
    <span class="write-line phone"></span>
  </div>

  <div class="stamp-grid">
    <span class="stamp"></span><span class="stamp"></span><span class="stamp"></span><span class="stamp"></span><span class="stamp"></span><span class="stamp"></span><span class="stamp"></span>
    <span class="stamp"></span><span class="stamp"></span><span class="stamp"></span><span class="stamp"></span><span class="stamp"></span><span class="stamp"></span><span class="stamp"></span>
  </div>

  <div class="business-name"><span class="name">The Lantern</span><span class="descriptor">COFFEE BAR &amp; GRILL</span></div>
  <div class="address">14b Wattlebrook St, Kelmarra NSW 2318, Ph. 02 4817 6293</div>
</section>

</body>
</html>
```